Local massage therapist needs some new marketing material

Hi there! I am a massage therapist here in Denver, CO in Willow Basin(shopping and art district) of the city. My business is called Lotus Drift Massage of Denver. My practice has an eastern influence and I do reflexology, thai massage and use Chinese herbs, etc. I know all my clients and pay close attention to details. I am also very respectful of tradition and it shows in how I work. I tend to like modern, clean, fun, Asian designs. I am wanting a new business card and brochure. I have a logo and branding for my business that I want used in the design. Currently, the sign for my building is purple and I think my logo was designed to be purple. I will attach pictures of it and can send whatever files are necessary so it can be integrated into the brochure, etc. I like the purple but open to using other colors as well. Thanks!
My website is lotusdriftmassagehub.example where info can be gathered about me and services/fees for brochure.
Updates

Just increased budget. Please see new feedback in discussion thread.

Thanks!

                                       HEY ALL,

Just wanted to let you know that I made a change to my website. It is on the Prices Page. I no longer have the frequent  flyer prices but I added discounts. Let me know if you have any questions. Thanks so much!

Target Market(s)

healthy, urban, educated, upper middle class, yogis

Industry/Entity Type

Marketing

Requirements
Must have
• logo stays purple
Should not have
• not too busy

```html
<!DOCTYPE html>
<html lang="en">
<head>
<meta charset="utf-8">
<title>Lotus Drift Massage of Denver – Brochure Spread</title>
<link href="https://fonts.googleapis.com/css2?family=Raleway:wght@300;400;600&family=Roboto+Condensed:wght@700&family=Great+Vibes&family=Questrial&display=swap" rel="stylesheet">
<style>
:root{
  --purple:#5c1a80;
  --pink:#e0148c;
  --gold:#f1d86c;
  --ink:#1d1d1d;
  --rule:#9a9a9a;
  --white:#ffffff;
  --photo-warm-a:#c9a08a;
  --photo-warm-b:#8a5a45;
  --photo-soft-a:#efe4dc;
  --photo-soft-b:#c7a894;
}
*{box-sizing:border-box;margin:0;padding:0}
html,body{width:1200px;height:849px;overflow:hidden;background:var(--white)}
.spread{position:relative;width:1200px;height:849px;border:1px solid var(--rule);font-family:"Questrial",sans-serif;color:var(--ink)}
.spread__fold{position:absolute;left:596px;top:0;width:1px;height:849px;background:var(--rule)}
.block{position:absolute}
.tile--purple{background:var(--purple)}
.photo{background:linear-gradient(135deg,var(--photo-soft-a),var(--photo-soft-b))}
.photo--warm{background:linear-gradient(135deg,var(--photo-warm-a),var(--photo-warm-b))}
.photo--candles{background:linear-gradient(160deg,#6b5a3a,#2f2a22)}

.title{position:absolute;left:340px;top:30px;width:240px}
.title__top{font-family:"Raleway",sans-serif;font-weight:300;font-size:31px;letter-spacing:.5px;margin-left:30px;line-height:1}
.title__script{font-family:"Great Vibes",cursive;color:var(--pink);font-size:52px;line-height:.9;margin-top:-4px}

.copy{position:absolute;font-size:7.7px;line-height:10.4px;text-align:justify}
.copy h2{font-family:"Roboto Condensed",sans-serif;font-weight:700;color:var(--pink);font-size:10px;letter-spacing:.2px;margin:9px 0 2px;text-transform:uppercase}
.copy h2:first-child{margin-top:0}
.copy p{margin:0}

.brand-vertical{position:absolute;left:232px;top:300px;width:70px;height:445px;display:flex;align-items:center;justify-content:center}
.brand-vertical span{transform:rotate(-90deg);white-space:nowrap;font-family:"Questrial",sans-serif;font-size:50px;letter-spacing:8px;color:var(--purple)}

.photo-strip{position:absolute;left:597px;top:38px;width:568px;height:227px;background:linear-gradient(120deg,#d9c2b0,#a8785f 45%,#6a4a3a 70%,#e7e2de)}
.photo-strip__gap{position:absolute;background:var(--white)}

.prices{position:absolute;left:597px;top:283px;width:288px;height:543px;background:var(--purple);color:var(--white)}
.prices__title{font-family:"Great Vibes",cursive;color:var(--gold);font-size:36px;text-align:center;margin-top:6px;line-height:1}
.prices__sub{font-family:"Raleway",sans-serif;font-size:17px;text-align:center;margin-top:10px;letter-spacing:.3px}
.rates{position:absolute;left:22px;top:82px;width:244px;display:flex}
.rate{flex:1;text-align:center;border-left:2px solid var(--white)}
.rate:first-child{border-left:none}
.rate__badge{width:68px;height:68px;border-radius:50%;background:var(--white);color:var(--pink);font-family:"Raleway",sans-serif;font-size:28px;display:flex;align-items:center;justify-content:center;margin:0 auto}
.rate__label{font-family:"Raleway",sans-serif;font-size:16px;line-height:23px;margin-top:6px}
.addon{position:absolute;left:28px;width:240px;display:flex;align-items:center;justify-content:space-between;font-size:9px;line-height:12px}
.addon__price{width:34px;height:34px;border-radius:50%;background:var(--white);color:var(--pink);font-family:"Raleway",sans-serif;font-size:15px;display:flex;align-items:center;justify-content:center;flex:none}
.cancel{position:absolute;left:17px;top:301px;width:263px;height:16px;background:var(--white);color:var(--purple);font-size:11px;text-align:center;line-height:16px}
.discounts{position:absolute;left:28px;top:326px;width:240px;font-size:8.6px;line-height:11.4px}
.discounts h3{font-family:"Roboto Condensed",sans-serif;font-size:11px;font-weight:700;margin-bottom:2px}
.discounts p{margin-bottom:11px}
.discounts .hl{color:var(--gold)}
</style>
</head>
<body>
<main class="spread">
  <div class="spread__fold"></div>

  <!-- left page tiles -->
  <div class="block tile--purple" style="left:38px;top:38px;width:130px;height:110px"></div>
  <div class="block photo photo--warm" style="left:175px;top:38px;width:131px;height:110px" role="img" aria-label="Woman relaxing on a massage table"></div>
  <div class="block photo photo--candles" style="left:38px;top:155px;width:130px;height:117px" role="img" aria-label="Candles and stacked stones by water"></div>
  <div class="block tile--purple" style="left:175px;top:155px;width:131px;height:117px"></div>

  <header class="title">
    <div class="title__top">VARIETIES OF</div>
    <div class="title__script">Massages</div>
  </header>

  <section class="copy" style="left:315px;top:131px;width:247px">
    <h2>Swedish Escape</h2>
    <p>Swedish Massage is a very relaxing and therapeutic style of bodywork. It combines oils with an array of strokes such as rolling, kneading, and percussion to help the body improve its circulation. The benefits of this type of bodywork are wide-ranging and include relief from aches and pains, decreased stress levels in the body, enhanced mental clarity, improved appearance, and greater flexibility.</p>
    <h2>Deep Tissue Therapy</h2>
    <p>Deep tissue massage is designed to relieve severe tension in the muscle and the connective tissue . This type of massage focuses on</p>
  </section>

  <section class="copy" style="left:38px;top:290px;width:188px">
    <p>the muscles located below the surface of the top muscles. Deep tissue massage is often recommended for individuals who experience consistent pain, are involved in heavy physical activity, and who have sustained physical injury. It is not uncommon for receivers of deep tissue massage to have their pain replaced with a new muscle ache for a day or two. Multiple sessions may be required in order to see consistent results and meet goals of becoming pain free.</p>
    <h2 style="margin-top:13px">Table Thai Massage</h2>
    <p>Table Thai Massage is an adaptation of the Traditional Thai Massage. It is performed on a massage table rather than on the floor. During Table Thai Massage, the client is fully clothed (loose-fitted) and no oil/lotion is used. It combines rhythmic rocking, compressions, acupressure and assisted yoga-like stretches to help lengthen shortened muscles and bring the body back into a state of balance.</p>
    <p>Thai massage is different from conventional massage because it does not work specifically with muscles and soft tissue, but rather it works along energy lines, or sen lines. The intention of Thai massage is to balance out the bodies energy and maintain a good energy flow along these Sen lines. The lines themselves run throughout the body in channels or paths, and if these channels become blocked, illness and disease begin to form in the body. By working along the sen lines, the channels can be cleared and allow the flow of energy to be restored, thus making the client feel uplifted and energized.</p>
    <h2 style="margin-top:13px">Blend Massage:</h2>
    <p>Blend Massage incorporates all techniques into one fully restorative and therapeutic session. Enjoy the benefits of soothing Swedish strokes, attention to Thai Sen lines, gentle stretching and deep pressure to relieve accumulated muscle tension and stress. This is the most popular modality.</p>
  </section>

  <div class="brand-vertical"><span>LOTUS DRIFT</span></div>

  <div class="block photo" style="left:330px;top:300px;width:267px;height:278px" role="img" aria-label="Woman receiving a head massage beside towels, shells and oil jars"></div>
  <div class="block tile--purple" style="left:330px;top:598px;width:128px;height:120px"></div>
  <div class="block photo" style="left:465px;top:598px;width:132px;height:112px" role="img" aria-label="Woman receiving a back massage"></div>
  <div class="block photo" style="left:330px;top:725px;width:128px;height:100px" role="img" aria-label="Man receiving a facial massage"></div>
  <div class="block tile--purple" style="left:465px;top:717px;width:132px;height:108px"></div>

  <!-- right page -->
  <div class="photo-strip" role="img" aria-label="Man relaxing during a hot stone massage">
    <div class="photo-strip__gap" style="left:131px;top:0;width:7px;height:227px"></div>
    <div class="photo-strip__gap" style="left:265px;top:0;width:7px;height:227px"></div>
    <div class="photo-strip__gap" style="left:401px;top:0;width:7px;height:227px"></div>
    <div class="photo-strip__gap" style="left:0;top:110px;width:568px;height:7px"></div>
  </div>

  <section class="prices">
    <div class="prices__title">Price List</div>
    <div class="prices__sub">STANDARD PRICES</div>
    <div class="rates">
      <div class="rate"><div class="rate__badge">$50</div><div class="rate__label">1 Hour<br>Massage</div></div>
      <div class="rate"><div class="rate__badge">$65</div><div class="rate__label">1-1/2 Hour<br>Massage</div></div>
      <div class="rate"><div class="rate__badge">$80</div><div class="rate__label">2 Hour<br>Massage</div></div>
    </div>
    <div class="addon" style="top:213px"><span>Add: Fire Cupping, Thai Herbal Compress<br>or Reflexology</span><span class="addon__price">$10</span></div>
    <div class="addon" style="top:255px"><span>Add: Hot Stones</span><span class="addon__price">$15</span></div>
    <div class="cancel">Cancellation Fee*$25 for each hour booked</div>
    <div class="discounts">
      <h3>DISCOUNTS</h3>
      <p><span class="hl">Massage Punch Card:</span> Upon your initial visit, you will receive your first punch. After 9 massages at the regular price, you will earn a free 1 hour massage of your choice. Referral Program: Get $10 off for every referral you make that comes in for a session. Gift certificates purchased for new clients will count toward the discount.</p>
      <p>Seniors, Students &amp; Educators: Ask about your discount.</p>
      <p>* 24 Hour Cancellations Policy applies to all Massage.</p>
      <p>*Prices are subject to change.</p>
    </div>
  </section>

  <section class="copy" style="left:895px;top:288px;width:260px">
    <h2>Prenatal Bliss:</h2>
    <p>Prenatal massage has been found to reduce stress, decrease swelling in the arms and legs, and relieve aches and pains in muscles and joints. Not only can massage be physically beneficial, but the human touch can be comforting and provide emotional support during pregnancy. Massage therapy has been found to reduce anxiety and depression. Massage is best to start during the second trimester.<br>Extra Massage Treats</p>
    <h2 style="margin-top:12px">Chinese Fire Cupping:</h2>
    <p>Cupping Method that uses glass cups to create a vacuum on the skin of the back. The suction penetrates deep into the tissues, allowing them to relax and release toxins. It triggers the lymphatic system, clears the blood vessels, loosens tight muscles, and stimulates the skin.</p>
    <h2 style="margin-top:12px">Hot Stones:</h2>
    <p>Hot stones (local basalt Colorado rocks) incorporates the use of smooth heated stones for a deeply soothing and relaxing experience. The stones are either used as part of a traditional swedish session or placed along specific areas of muscle tension to reduce discomfort and increase circulation. A nice treat after a long day or during the winter season.</p>
    <h2 style="margin-top:12px">Reflexology:</h2>
    <p>A modality focused on the feet. It is a non-invasive way to work the entire body system. Pressure is applied to various reflexes on the foot in order to promote balance and healing in the body. Certain areas of the foot correspond to organs and specific parts of the body. Reflexology helps to clear blocked energy, balance emotions and relax the body.</p>
    <h2 style="margin-top:12px">Thai Herbal Compress:</h2>
    <p>Hand-made herbal compresses imported from Thailand make for a truly delightful and unique experience. The steamed herbal compress is applied directly to the body and helps relieve sore muscles while the aroma soothes the mind.</p>
  </section>
</main>
</body>
</html>
```